33.5 x 80 - Retractable Banner - Bluecrane Lending Group Inc.

Bluecrane Lending Group, Inc.

A Community Based Mortgage Broker
Offering a Full Line of Mortgage Loan Products

Home of the Mortgage Originating Real Estate Experts

"Trust the Bluecrane, we'll guide you home"

Licensed in DC, MD and VA

EST 1997
NMLS #517638
Phone (800) 946-2071
www.bluecranehub.example
www.jobswithbluecrane.exampl
@flywithbluecrane

```html
<!DOCTYPE html>
<html lang="en">
<head>
<meta charset="utf-8">
<title>Bluecrane Lending Group – Retractable Banner</title>
<link href="https://fonts.googleapis.com/css2?family=Roboto+Condensed:ital,wght@0,400;0,700;1,700&display=swap" rel="stylesheet">
<style>
  :root {
    --canvas: #000000;
    --paper: #ffffff;
    --brand-blue: #2c3f97;
    --brand-blue-deep: #1f2f7a;
    --brand-gold: #f0b72f;
    --ink: #1c1c1c;
    --photo-light: #eef0f2;
    --photo-mid: #c9c6bf;
  }
  * { margin: 0; padding: 0; box-sizing: border-box; }
  html, body {
    width: 1200px; height: 1200px; overflow: hidden;
    background: var(--canvas);
    font-family: "Roboto Condensed", "Arial Narrow", sans-serif;
  }
  .banner {
    position: absolute; left: 408px; top: 139px;
    width: 384px; height: 917px;
    background: var(--paper); overflow: hidden;
  }
  .banner-shapes { position: absolute; inset: 0; }
  .brand {
    position: absolute; right: 26px; top: 44px; width: 190px;
    text-align: center; color: var(--brand-blue);
  }
  .brand-mark {
    width: 34px; height: 34px; border-radius: 50%;
    background: var(--brand-gold); margin: 0 auto 6px;
  }
  .brand-name { font-size: 19px; font-weight: 700; line-height: 1.05; text-transform: uppercase; }
  .brand-tagline { font-size: 8px; font-weight: 400; margin-top: 4px; color: var(--ink); }
  .brand-est { font-size: 8px; font-weight: 400; color: var(--ink); }
  .intro {
    position: absolute; right: 24px; top: 158px; text-align: right;
    color: var(--ink); font-size: 13.5px; line-height: 1.2;
  }
  .intro-motto { color: var(--brand-blue); font-weight: 700; font-size: 12.5px; margin-top: 5px; line-height: 1.15; }
  .headline {
    position: absolute; left: 0; right: 0; top: 262px; text-align: center;
    color: var(--brand-blue); font-weight: 700; font-size: 37px; line-height: 1.05;
    letter-spacing: -0.5px;
  }
  .license-seal {
    position: absolute; left: 12px; top: 638px; width: 122px; height: 122px;
    border-radius: 50%; background: var(--brand-blue);
    border: 5px solid var(--paper);
    display: flex; align-items: center; justify-content: center; text-align: center;
    color: var(--paper); font-weight: 700; font-size: 18px; line-height: 1.1;
  }
  .details {
    position: absolute; left: 0; right: 0; top: 770px; text-align: center;
    color: var(--paper); font-size: 13px; line-height: 2.1;
  }
  .details .phone { font-weight: 700; }
  .web-links {
    position: absolute; left: 31px; right: 31px; top: 870px; height: 28px;
    border-radius: 14px; background: var(--paper); color: var(--brand-blue);
    font-size: 11px; font-weight: 700;
    display: flex; align-items: center; justify-content: center;
  }
</style>
</head>
<body>
<main class="banner">
  <svg class="banner-shapes" width="384" height="917" viewBox="0 0 384 917">
    <defs>
      <clipPath id="inner-circle"><circle cx="205" cy="390" r="325"/></clipPath>
      <linearGradient id="portrait-tones" x1="0" y1="0" x2="1" y2="1">
        <stop offset="0" stop-color="var(--photo-light)"/>
        <stop offset="0.5" stop-color="var(--photo-mid)"/>
        <stop offset="1" stop-color="var(--photo-light)"/>
      </linearGradient>
    </defs>
    <circle class="ring-blue" cx="205" cy="390" r="385" fill="none" stroke="var(--brand-blue)" stroke-width="30"/>
    <circle class="ring-gold" cx="205" cy="390" r="348" fill="var(--paper)" stroke="var(--brand-gold)" stroke-width="44"/>
    <rect class="portrait" x="0" y="350" width="384" height="320" fill="url(#portrait-tones)" clip-path="url(#inner-circle)" role="img" aria-label="Photo of a relaxed businessman in a light suit leaning back with hands behind his head"/>
    <path class="footer-panel" d="M0 700 Q192 650 384 690 L384 917 L0 917 Z" fill="var(--brand-blue)"/>
    <path class="footer-accent" d="M0 690 Q192 640 384 680" fill="none" stroke="var(--paper)" stroke-width="6"/>
  </svg>

  <header class="brand">
    <div class="brand-mark"></div>
    <div class="brand-name">Bluecrane Lending Group</div>
    <div class="brand-tagline">Guiding families home, one step forward</div>
    <div class="brand-est">EST. 1997</div>
  </header>

  <section class="intro">
    <p>A Community Based Mortgage Broker<br>Offering a Full Line of Mortgage Loan Products</p>
    <p class="intro-motto">Home of the Mortgage Originating<br>Real Estate Experts</p>
  </section>

  <h1 class="headline">Trust the Bluecrane,<br>we'll guide you home.</h1>

  <div class="license-seal">Licensed in<br>DC, MD and<br>VA</div>

  <section class="details">
    <p>EST 1997</p>
    <p>NMLS #517638</p>
    <p class="phone">Phone (800) 946-2071 &nbsp;|&nbsp; @flywithbluecrane</p>
  </section>

  <div class="web-links">www.bluecranehub.example &nbsp;|&nbsp; www.jobswithbluecrane.exampl</div>
</main>
</body>
</html>
```